Small Production Wine Needs a Wine Label Design

We need a wine bottle label design for a hand crafted Petite Sirah wine produced by two friends in the wine industry. The wine brand will be called, TK (the first initials of each of their last names, Tavares Kimble). The petite sirah grapes are from the Tavares vineyard in the Russian River Valley of Sonoma County, and Kimble is the winemaker. Tavares is a third generation farmer in sonoma county and also raised cattle on the same ranch the grapes were grown. Kimble is an experienced Winemaker and helped increase the quality of wines from Lodi, CA at a small boutique winery. For the front label, we would like the TK to look like a cattle brand, the font to be color black. We would like to include somewhere on the label Tavares Kimble, maybe underneath the cattle brand in smaller font. We also need to include the appellation on the label, Russian River Valley, and in smaller font Sonoma County. Also, the varietal of the wine is Petite Sirah and the vintage is 2013. We are aiming for a simple and relatively classy label, yet with a rustic touch. We would like the label to be rectangular and have an organic/linen look to it. Also the incorporation of a ridge or mountain range in the back ground or subtly in the label would be cool.

```html
<!DOCTYPE html>
<html lang="en">
<head>
<meta charset="utf-8">
<title>Tavares Kimble Petite Sirah 2013 Label</title>
<link href="https://fonts.googleapis.com/css2?family=Marcellus&display=swap" rel="stylesheet">
<style>
  :root {
    --label-black: #050505;
    --silver-light: #f4f4f4;
    --silver-mid: #c9c9c9;
    --silver-dark: #8e8e8e;
    --text-white: #f2f2f2;
    --ink: #0a0a0a;
  }
  html, body {
    margin: 0;
    padding: 0;
    width: 865px;
    height: 1200px;
    overflow: hidden;
    background: var(--label-black);
  }
  .label {
    position: relative;
    width: 865px;
    height: 1200px;
    background: var(--label-black);
    font-family: "Marcellus", "Optima", serif;
    color: var(--text-white);
  }
  .label__frame {
    position: absolute;
    inset: 10px;
    border: 22px solid transparent;
    border-image: linear-gradient(135deg, var(--silver-dark), var(--silver-light) 35%, var(--silver-mid) 60%, var(--silver-light) 85%, var(--silver-dark)) 1;
  }
  .label__inner-rule {
    position: absolute;
    inset: 44px;
    border: 2px solid var(--silver-mid);
  }
  .label__ridge {
    position: absolute;
    left: 100px;
    top: 88px;
    width: 660px;
    height: 230px;
    background: radial-gradient(ellipse at 55% 55%, rgba(220,220,220,0.55), rgba(140,140,140,0.25) 45%, rgba(5,5,5,0) 72%);
  }
  .brand {
    position: absolute;
    left: 0;
    top: 300px;
    width: 865px;
    height: 520px;
  }
  .brand__mark {
    position: absolute;
    left: 0;
    right: 0;
    top: 40px;
    text-align: center;
    font-size: 330px;
    line-height: 1;
    letter-spacing: 6px;
    color: var(--silver-mid);
  }
  .brand__name {
    position: absolute;
    top: 330px;
    font-size: 31px;
    letter-spacing: 1px;
    color: var(--text-white);
  }
  .brand__name--first { left: 172px; }
  .brand__name--second { left: 455px; }
  .varietal {
    position: absolute;
    left: 62px;
    top: 851px;
    width: 740px;
    height: 66px;
    background: linear-gradient(90deg, var(--silver-dark), var(--silver-light) 30%, var(--silver-light) 60%, var(--silver-mid));
    color: var(--ink);
    font-size: 36px;
    line-height: 66px;
    text-align: center;
    letter-spacing: 1px;
  }
  .appellation {
    position: absolute;
    left: 0;
    right: 0;
    top: 950px;
    text-align: center;
    font-size: 42px;
    line-height: 1;
    letter-spacing: 1px;
  }
  .appellation__county {
    display: block;
    margin-top: 12px;
    font-size: 27px;
  }
  .vintage {
    position: absolute;
    right: 64px;
    top: 1100px;
    font-size: 32px;
  }
</style>
</head>
<body>
  <main class="label">
    <div class="label__frame"></div>
    <div class="label__inner-rule"></div>
    <div class="label__ridge" role="img" aria-label="Silver mountain ridge illustration"></div>
    <div class="brand">
      <div class="brand__mark">TK</div>
      <span class="brand__name brand__name--first">TAVARES</span>
      <span class="brand__name brand__name--second">KIMBLE</span>
    </div>
    <div class="varietal">PETITE SIRAH</div>
    <div class="appellation">
      RUSSIAN RIVER VALLEY
      <span class="appellation__county">SONOMA COUNTY</span>
    </div>
    <div class="vintage">2013</div>
  </main>
</body>
</html>
```